Stationary, Envelope, Folder, Brochure
brightmendhome.example
Stationary, Envelope, Folder, Brochure - Health
Creative Brief
Health
Corporate, and Patients. Something bright and uplifting to grab the brightmend home feeling when people look at our materials. I like the QVR Petal Courier Lad logo and some of the materials they use. It has an uplifting look and feel.
Provide the materials listed in the Title. Use the uploaded picture logo.
quietharborwatch quietharborwatch
Colors: I do like the Blues and the gradient from a darker to a brighter blue. Maybe even do that more with other bright colors. Have fun explore a little and think outside the box. Will try to provide with as much feedback as possible. -Desmond
Hi Everyone, Keep in mind we want a look and feel of "BRIGHT Mend Home" and putting the "Care" back into healthcare. Having a bright and professional look that will excite the senses when a person looks at the material. We do not want to be the "norm" of home health. Our clients are of all ages for example 20+. Lets get excited, creative, and see what we can come up with. Also "Brightmend Home" Font needs to also be fun and represent the logo and spirit of the great experience our company provide unlike others.

```html
<!DOCTYPE html>
<html lang="en">
<head>
<meta charset="utf-8">
<title>Brightmend Home – Stationery Set</title>
<link href="https://fonts.googleapis.com/css2?family=Montserrat:wght@400;600;700&family=Open+Sans:wght@400;600&display=swap" rel="stylesheet">
<style>
  :root{
    --board:#8c8d8f;
    --label:#eef0f2;
    --navy:#0a2744;
    --deep:#0b4a78;
    --blue:#137cb6;
    --cyan:#2fb3e2;
    --paper:#ffffff;
    --ink:#2c3e50;
    --muted:#9aa8b4;
    --photo-warm:#d9a57a;
    --photo-sea:#3f6f92;
  }
  *{box-sizing:border-box;margin:0;padding:0}
  html,body{width:1200px;height:389px;overflow:hidden}
  body{background:var(--board);font-family:"Open Sans",Arial,sans-serif;position:relative;color:var(--ink)}
  .piece{position:absolute;background:var(--paper);box-shadow:0 2px 5px rgba(0,0,0,.35);overflow:hidden}
  .piece-label{position:absolute;font:600 5px "Montserrat",Arial,sans-serif;letter-spacing:.6px;color:var(--label);text-transform:uppercase;text-align:center}
  .gradient{background:linear-gradient(135deg,var(--navy) 0%,var(--deep) 45%,var(--blue) 75%,var(--cyan) 100%)}
  .brand{font:700 8px "Montserrat",Arial,sans-serif;letter-spacing:.6px;color:#fff;text-transform:uppercase;display:flex;align-items:center;gap:3px;white-space:nowrap}
  .brand::before{content:"";width:6px;height:6px;border-radius:50%;background:currentColor;display:block;flex:none}
  .brand.on-paper{color:var(--blue)}
  .brand.stacked{white-space:normal;align-items:flex-start;line-height:1.2;letter-spacing:.2px}
  .brand.stacked::before{width:4px;height:4px;margin-top:1px}
  .photo{position:absolute}
  .photo-portrait{background:linear-gradient(160deg,#cfd9e2,#8fa9bf 60%,#5b7f9f)}
  .photo-dock{background:linear-gradient(180deg,#f4c38a 0%,var(--photo-warm) 35%,#6f7f9a 60%,var(--photo-sea) 100%)}
  .photo-hands{background:linear-gradient(150deg,#efd2b8,#c99b7b 55%,#9d7b67)}
  .swoosh{position:absolute;left:0;width:100%}
  .copy{position:absolute;font-size:4px;line-height:6px;color:var(--ink)}
  .copy h4{font:700 6px "Montserrat",Arial,sans-serif;color:var(--blue);margin-bottom:2px}
  .rule{height:1px;background:#d5dde4;margin:4px 0}
  .tagline{font:600 8px "Montserrat",Arial,sans-serif;color:#fff;line-height:10px}
</style>
</head>
<body>

<div class="piece-label" style="left:10px;top:4px;width:160px">Brochure</div>
<section class="piece brochure-outside" style="left:10px;top:14px;width:160px;height:166px">
  <div class="photo photo-portrait" role="img" aria-label="Photo of a smiling caregiver" style="left:0;top:0;width:54px;height:166px"></div>
  <div class="copy" style="left:58px;top:14px;width:46px">
    <h4>Our Services</h4>
    Nursing visits at home<br>Daily living support<br>Therapy and recovery<br>Family guidance
  </div>
  <div class="gradient" style="position:absolute;left:107px;top:0;width:53px;height:166px">
    <div class="brand stacked" style="position:absolute;left:5px;top:58px;width:44px;font-size:5px">Brightmend Home</div>
    <div class="tagline" style="position:absolute;left:5px;top:80px;font-size:5px;line-height:7px">Care with a<br>human touch</div>
  </div>
</section>

<div class="piece-label" style="left:180px;top:4px;width:160px">Brochure Inside</div>
<section class="piece brochure-inside" style="left:180px;top:14px;width:160px;height:166px">
  <div class="photo photo-dock" role="img" aria-label="Photo of a wooden dock at sunset over water" style="left:0;top:0;width:160px;height:80px"></div>
  <svg class="swoosh" style="top:68px" width="160" height="20" viewBox="0 0 160 20" aria-hidden="true">
    <path d="M0 20 C50 0 110 0 160 8 L160 20 Z" fill="#fff"/>
  </svg>
  <div class="copy" style="left:8px;top:90px;width:66px">
    <h4>Who We Are</h4>
    We bring calm and skilled care into every home we visit.
    <div class="rule"></div>
    Trusted by families of all ages.
  </div>
  <div class="copy" style="left:84px;top:90px;width:68px">
    <h4>Why Choose Us</h4>
    Caring staff, flexible hours and plans made for you.
  </div>
</section>

<div class="piece-label" style="left:10px;top:186px;width:160px">Postcard</div>
<section class="piece postcard" style="left:10px;top:196px;width:160px;height:188px">
  <div class="gradient" style="position:absolute;left:0;top:0;width:160px;height:60px">
    <div class="brand" style="position:absolute;left:10px;top:24px">Brightmend Home</div>
  </div>
  <div class="copy" style="left:10px;top:68px;width:140px">
    <h4>Care that comes home</h4>
    Call today to plan a visit with our friendly team.
  </div>
  <div class="photo photo-hands" role="img" aria-label="Photo of caring hands held together" style="left:0;top:108px;width:160px;height:80px"></div>
</section>

<div class="piece-label" style="left:180px;top:186px;width:160px">Mailer Postcard</div>
<section class="piece mailer-postcard" style="left:180px;top:196px;width:160px;height:188px">
  <div class="photo photo-dock" role="img" aria-label="Photo of a calm lake at dusk" style="left:0;top:0;width:160px;height:78px"></div>
  <div class="copy" style="left:10px;top:88px;width:140px">
    <h4>Bright care, every day</h4>
    Visit brightmendhome.example to learn more.
  </div>
  <div class="gradient" style="position:absolute;left:0;bottom:0;width:160px;height:20px"></div>
</section>

<div class="piece-label" style="left:384px;top:4px;width:180px">Folder</div>
<section class="piece folder-cover gradient" style="left:384px;top:14px;width:180px;height:214px">
  <svg class="swoosh" style="top:20px" width="180" height="120" viewBox="0 0 180 120" aria-hidden="true">
    <path d="M0 90 C60 40 120 30 180 0" stroke="rgba(255,255,255,.18)" stroke-width="14" fill="none"/>
    <path d="M0 110 C70 60 130 55 180 30" stroke="rgba(255,255,255,.1)" stroke-width="6" fill="none"/>
  </svg>
  <div class="brand" style="position:absolute;left:52px;top:62px;font-size:9px">Brightmend Home</div>
  <div class="tagline" style="position:absolute;left:60px;top:128px">Bright care<br>with a<br>human touch</div>
</section>

<section class="piece folder-open" style="left:350px;top:236px;width:286px;height:148px">
  <div style="position:absolute;left:142px;top:0;width:2px;height:148px;background:#e1e6ea"></div>
  <svg class="swoosh" style="top:88px" width="286" height="60" viewBox="0 0 286 60" aria-hidden="true">
    <path d="M0 60 L0 20 C40 5 90 5 143 18 L143 60 Z" fill="#f1f4f6"/>
    <path d="M143 60 L143 18 C190 5 240 5 286 20 L286 60 Z" fill="#f1f4f6"/>
  </svg>
  <div style="position:absolute;left:210px;top:112px;width:36px;height:20px;border:1px solid #cfd7de"></div>
</section>

<div class="piece-label" style="left:660px;top:12px;width:130px">Original Card</div>
<section class="piece card-front gradient" style="left:660px;top:22px;width:130px;height:76px">
  <div class="brand" style="position:absolute;left:28px;top:32px">Brightmend Home</div>
</section>
<section class="piece card-back" style="left:660px;top:106px;width:130px;height:76px">
  <div class="copy" style="left:8px;top:10px;width:80px">
    <h4>Desmond Hale</h4>
    Care Director<br>555 010 2244<br>brightmendhome.example
  </div>
  <svg class="swoosh" style="bottom:0" width="130" height="18" viewBox="0 0 130 18" aria-hidden="true">
    <defs><linearGradient id="cb" x1="0" x2="1"><stop offset="0" stop-color="#0a2744"/><stop offset="1" stop-color="#2fb3e2"/></linearGradient></defs>
    <path d="M0 18 L0 10 C40 0 90 0 130 8 L130 18 Z" fill="url(#cb)"/>
  </svg>
</section>

<div class="piece-label" style="left:680px;top:218px;width:100px">Vertical Card</div>
<section class="piece card-vertical" style="left:680px;top:228px;width:100px;height:144px">
  <div class="gradient" style="position:absolute;left:0;top:0;width:100px;height:86px">
    <div class="brand" style="position:absolute;left:0;top:38px;width:100px;justify-content:center;font-size:5.5px;letter-spacing:.3px">Brightmend Home</div>
  </div>
  <svg class="swoosh" style="top:72px" width="100" height="16" viewBox="0 0 100 16" aria-hidden="true">
    <path d="M0 16 C30 2 70 2 100 12 L100 16 Z" fill="#fff"/>
  </svg>
  <div class="copy" style="left:10px;top:96px;width:80px;text-align:center">
    Desmond Hale<br>555 010 2244<br>brightmendhome.example
  </div>
</section>

<div class="piece-label" style="left:840px;top:4px;width:144px">Letterhead</div>
<section class="piece letterhead" style="left:840px;top:14px;width:144px;height:214px">
  <div class="brand on-paper" style="position:absolute;left:12px;top:12px;font-size:6px">Brightmend Home</div>
  <svg class="swoosh" style="top:70px" width="144" height="80" viewBox="0 0 144 80" aria-hidden="true">
    <path d="M0 70 C50 20 100 20 144 0" stroke="#eef3f7" stroke-width="12" fill="none"/>
  </svg>
  <svg class="swoosh" style="bottom:0" width="144" height="22" viewBox="0 0 144 22" aria-hidden="true">
    <defs><linearGradient id="lh" x1="0" x2="1"><stop offset="0" stop-color="#0a2744"/><stop offset="1" stop-color="#2fb3e2"/></linearGradient></defs>
    <path d="M0 22 L0 12 C50 0 100 0 144 10 L144 22 Z" fill="url(#lh)"/>
  </svg>
</section>

<div class="piece-label" style="left:1008px;top:4px;width:168px">Fax Sheet</div>
<section class="piece fax-sheet" style="left:1008px;top:14px;width:168px;height:214px">
  <div class="gradient" style="position:absolute;left:0;top:0;width:168px;height:18px"></div>
  <div class="brand on-paper" style="position:absolute;left:12px;top:26px;font-size:6px">Brightmend Home</div>
  <div class="copy" style="left:12px;top:46px;width:144px">
    <h4>Fax</h4>
    To:<div class="rule"></div>
    From:<div class="rule"></div>
    Date:<div class="rule"></div>
    Pages:<div class="rule"></div>
  </div>
  <div style="position:absolute;left:12px;top:120px;width:144px;height:60px;border:1px solid #d5dde4"></div>
</section>

<section class="piece envelope" style="left:800px;top:290px;width:210px;height:94px">
  <div class="brand on-paper" style="position:absolute;left:10px;top:10px;font-size:6px">Brightmend Home</div>
  <div class="copy" style="left:10px;top:22px;width:80px;font-size:3.5px">brightmendhome.example</div>
  <svg class="swoosh" style="bottom:0" width="210" height="30" viewBox="0 0 210 30" aria-hidden="true">
    <defs><linearGradient id="ev" x1="0" x2="1"><stop offset="0" stop-color="#0a2744"/><stop offset="1" stop-color="#2fb3e2"/></linearGradient></defs>
    <path d="M0 30 L0 24 C80 6 150 2 210 10 L210 30 Z" fill="url(#ev)"/>
  </svg>
</section>

</body>
</html>
```